依頼詳細
小学校経由で小学生の皆さんに、チラシを配布いたします。岬野市、岬野市教育委員会の後援もとっており、夏休みの宿題対策ワークショップをするどのショッピングセンターよりも選んでいただける、楽しい見栄えの作品になればうれしいです。
記載項目
詳細は添付ファイルにて
サイズ
A4
ページ数
片面
希望イメージ
シンプル 複雑
単色 カラフル
暗い 明るい
日常 高級
遊び心 厳粛
未来的 伝統的
女性的 男性的
希望する色
黄・オレンジ系、青系、水色系
納品ファイル
• 高解像度JPG (.jpg)
• イラストレーター形式 (.ai)
• PNG形式 (.png)
補足説明
■ 選んだ理由

表面のみという表現場所で、内容がみやすく、かつ 大変華やかで
子ども達の目を引くデザインになっているところや、写真のロゴからの抽出で
うまく取り入れていただいたり、気の利いた内容でした

■ 提案者全員のお礼・コメント

たくさんのご応募いただき、まことにありがとうございました。
また、同じくコンペ形式でお世話になると思いますが、ぜひまたご提案ください。
よろしくお願いいたします。

```html
<!DOCTYPE html>
<html lang="ja">
<head>
<meta charset="utf-8">
<title>夏休みワークショップ</title>
<link rel="stylesheet" href="https://fonts.googleapis.com/css2?family=M+PLUS+Rounded+1c:wght@400;700;800;900&display=swap">
<style>
:root{
  --blue:#1d6cc0;
  --blue-deep:#0f4f98;
  --sky:#bfe3f7;
  --yellow:#ffe93a;
  --yellow-soft:#fff59e;
  --ink:#1d3550;
  --white:#ffffff;
}
*{margin:0;padding:0;box-sizing:border-box}
html,body{width:849px;height:1200px;overflow:hidden;background:var(--white)}
body{font-family:"M PLUS Rounded 1c",sans-serif;color:var(--ink)}
.flyer{position:relative;width:849px;height:1200px;overflow:hidden;background:var(--white)}
.abs{position:absolute;white-space:nowrap}
.deco{position:absolute;inset:0}

/* header */
.days-tag{left:680px;top:0;width:169px;height:62px;background:var(--blue);color:var(--white);
  font-weight:900;font-size:34px;display:flex;align-items:center;justify-content:center;border-bottom-left-radius:18px}
.dates{left:650px;top:72px;width:190px;height:160px;color:var(--blue);font-weight:900;line-height:1}
.dates .month{font-size:56px;position:absolute;left:0;top:20px}
.dates .day{position:absolute;left:84px;font-size:48px;display:flex;align-items:center;gap:6px}
.dates .dow{font-size:17px;background:var(--blue);color:var(--white);border-radius:50%;width:28px;height:28px;display:inline-flex;align-items:center;justify-content:center}
.title-main{left:140px;top:22px;font-size:122px;font-weight:900;color:var(--blue);letter-spacing:4px;line-height:1;
  text-shadow:6px 6px 0 var(--yellow)}
.title-sub{left:170px;top:168px;font-size:52px;font-weight:900;color:var(--blue);letter-spacing:2px;line-height:1.1}
.ticket{left:12px;top:96px;width:118px;height:118px;border-radius:50%;background:var(--yellow);color:var(--blue);
  display:flex;flex-direction:column;align-items:center;justify-content:center;text-align:center;font-weight:900;gap:4px}
.ticket .label{font-size:24px;line-height:1}
.ticket .time{font-size:14px;line-height:1}

.venue{left:150px;top:250px;color:var(--blue);font-weight:900;line-height:1.3}
.venue .tag{display:inline-block;background:var(--blue);color:var(--white);font-size:19px;padding:3px 9px;border-radius:8px;margin-right:8px;vertical-align:middle}
.venue .place{font-size:26px;vertical-align:middle}
.venue .court{font-size:26px;padding-left:90px}

.hours{left:636px;top:256px;width:200px;color:var(--blue);font-weight:900;text-align:center}
.hours .head{font-size:28px;line-height:1.2;border-bottom:3px solid var(--blue);padding-bottom:4px;margin-bottom:6px}
.hours .t{font-size:21px;line-height:1.5}
.hours .t b{font-size:38px}
.hours .note{font-size:13px;margin-top:4px;color:var(--ink);font-weight:700}

.capacity{left:0;top:592px;width:440px;height:96px;background:var(--sky);border-radius:0 48px 48px 0;display:flex;align-items:center;padding-left:14px;gap:12px}
.capacity .label{flex-shrink:0;width:38px;height:74px;background:var(--blue);color:var(--white);font-weight:900;font-size:20px;border-radius:8px;
  display:flex;align-items:center;justify-content:center;writing-mode:vertical-rl;letter-spacing:4px}
.capacity .rules{flex-shrink:0;background:var(--white);border-radius:8px;padding:6px 12px;color:var(--blue);font-weight:800;font-size:19px;line-height:1.45}
.capacity .small{font-size:11px;color:var(--ink);font-weight:700;line-height:1.6}

.fee{left:400px;top:692px;width:420px;height:48px;background:var(--yellow);border-radius:24px;color:var(--blue);
  font-weight:900;font-size:24px;display:flex;align-items:center;justify-content:center;gap:10px}
.fee .tag{background:var(--blue);color:var(--white);font-size:17px;padding:3px 10px;border-radius:14px}
.cash{left:730px;top:748px;font-size:13px;font-weight:800;color:var(--white);background:var(--blue);padding:2px 10px;border-radius:10px}
.homework{left:60px;top:738px;font-size:32px;font-weight:900;color:var(--blue);transform:rotate(-4deg)}

/* programme */
.program{left:14px;top:802px;width:821px;display:grid;grid-template-columns:repeat(3,1fr);gap:14px}
.day-col{display:flex;flex-direction:column;gap:8px}
.day-head{height:54px;background:var(--yellow);border-radius:27px;color:var(--blue);font-weight:900;font-size:34px;
  display:flex;align-items:center;justify-content:center;gap:8px;margin-bottom:2px}
.day-head .dow{font-size:16px;background:var(--blue);color:var(--white);border-radius:50%;width:30px;height:30px;display:inline-flex;align-items:center;justify-content:center}
.item{background:var(--white);border:3px solid var(--blue);border-radius:12px;padding:5px 12px;height:73px;display:flex;flex-direction:column;justify-content:space-between}
.item.compact{height:53px;padding:3px 12px}
.item .name{font-size:16px;font-weight:800;color:var(--ink);line-height:1.3}
.item .price{text-align:right;font-size:21px;font-weight:900;color:var(--blue);line-height:1.1}
.item .price small{font-size:13px}

/* footer */
.rule{left:0;top:1120px;width:849px;height:4px;background:var(--blue)}
.footer{left:0;top:1128px;width:849px;height:72px;background:var(--sky);padding:10px 20px;font-size:13px;font-weight:700;color:var(--ink);line-height:1.75}
.footer .row{display:flex;justify-content:space-between}
.footer b{color:var(--blue)}
</style>
</head>
<body>
<main class="flyer">
  <svg class="deco" width="849" height="1200" viewBox="0 0 849 1200" aria-hidden="true">
    <circle cx="610" cy="170" r="150" fill="var(--yellow-soft)"/>
    <circle cx="70" cy="660" r="64" fill="var(--yellow-soft)"/>
    <path d="M0 360 Q130 320 250 380 T520 400" fill="none" stroke="var(--yellow)" stroke-width="10" stroke-linecap="round"/>
    <circle cx="380" cy="440" r="14" fill="var(--yellow)"/>
    <circle cx="420" cy="480" r="8" fill="var(--sky)"/>
    <circle cx="560" cy="520" r="10" fill="var(--yellow)"/>
  </svg>

  <div class="abs days-tag">3 Days</div>
  <div class="abs dates">
    <span class="month">7/</span>
    <span class="day" style="top:0">29<span class="dow">金</span></span>
    <span class="day" style="top:54px">30<span class="dow">土</span></span>
    <span class="day" style="top:108px">31<span class="dow">日</span></span>
  </div>

  <h1 class="abs title-main">夏休み</h1>
  <p class="abs title-sub">ワークショップ</p>

  <div class="abs ticket"><span class="label">整理券</span><span class="time">午前10時から</span></div>

  <div class="abs venue">
    <div><span class="tag">会場</span><span class="place">みさきショッピングパークLuz内</span></div>
    <div class="court">セントラルコート</div>
  </div>

  <div class="abs hours">
    <div class="head">開催時間</div>
    <div class="t">午前<b>10</b>時から</div>
    <div class="t">午後<b>4</b>時ごろまで</div>
    <div class="note">なくなり次第終了</div>
  </div>

  <div class="abs capacity">
    <span class="label">定員</span>
    <div class="rules">1回 15家族様<br>おひとり様 1種類</div>
    <div class="small">※各日先着順です<br>※保護者の方も<br>　ご一緒にどうぞ</div>
  </div>

  <div class="abs fee"><span class="tag">参加費</span>200円か300円</div>
  <div class="abs homework">宿題はお早めに！</div>
  <div class="abs cash">現金のみ</div>

  <section class="abs program">
    <div class="day-col">
      <div class="day-head">7/29<span class="dow">金</span></div>
      <div class="item"><span class="name">オリジナル傘を作ろう</span><span class="price">300<small>円</small></span></div>
      <div class="item"><span class="name">ココロガーレ</span><span class="price">300<small>円</small></span></div>
      <div class="item"><span class="name">スクラッチアート</span><span class="price">200<small>円</small></span></div>
    </div>
    <div class="day-col">
      <div class="day-head">7/30<span class="dow">土</span></div>
      <div class="item"><span class="name">ペットボトルで貯金箱</span><span class="price">300<small>円</small></span></div>
      <div class="item"><span class="name">ひまわりリース</span><span class="price">300<small>円</small></span></div>
      <div class="item"><span class="name">風鈴を作ろう</span><span class="price">300<small>円</small></span></div>
    </div>
    <div class="day-col">
      <div class="day-head">7/31<span class="dow">日</span></div>
      <div class="item compact"><span class="name">和紙ランタンを作ろう</span><span class="price">300<small>円</small></span></div>
      <div class="item compact"><span class="name">走れ！風力カー！</span><span class="price">200<small>円</small></span></div>
      <div class="item compact"><span class="name">牛乳パック ペン立て</span><span class="price">200<small>円</small></span></div>
      <div class="item compact"><span class="name">くるくるランプ</span><span class="price">300<small>円</small></span></div>
    </div>
  </section>

  <div class="abs rule"></div>
  <footer class="abs footer">
    <div class="row"><span><b>運営会社：</b>株式会社Sunnyway(サニーウェイ)</span><span><b>問い合わせ先：</b>Email info@sunnyway-kids.jp</span></div>
    <div class="row"><span><b>主催：</b>みさきショッピングパークLuz　〒000-0000 岬野県岬野市中町 1-2-3</span><span><b>後援：</b>岬野市、岬野市教育委員会</span></div>
  </footer>
</main>
</body>
</html>
```